Rooted Plots: A Simple Handbook for Newcomers

I need a book cover design for a book showing a Permaculture Garden. The sub title is : Zero Skills Required, Easy-Care Methods For A Greener And Nature Kind Yard That Flourishes, Also On Tiny Balconies

Down to earth colors but with something bright to catch the eye

First time using this so my apologies. I believe I posted the colors which are good. I mentioned it is for Permaculture Gardening which is a lot different from just regular till and plant gardens. They tend to try not to dig too much, plant with other plants that help each other and let the dead stuff just rot into the ground so they automatically feed the soil around it.
I don’t want a white background ( someone else used, that is why I mention). Realistic (ish) Gardening type tools (no shovel 😀) like maybe a watering can or a marker for a type of plant, etc. I do want a brighter color somehow within to help catch the eye.

```html
<!DOCTYPE html>
<html lang="en">
<head>
<meta charset="utf-8">
<title>Rooted Plots: A Simple Handbook for Newcomers</title>
<link rel="stylesheet" href="https://fonts.googleapis.com/css2?family=Montserrat:wght@300;400;800&display=swap">
<style>
  :root {
    --page-bg: #c9a77a;
    --cover-bg: #0d2015;
    --leaf-green: #7fb81a;
    --ink-white: #ffffff;
    --band-red: #5d0b0a;
  }
  html, body {
    margin: 0;
    padding: 0;
    width: 1200px;
    height: 1200px;
    overflow: hidden;
    background: var(--page-bg);
  }
  .book-cover {
    position: absolute;
    left: 264px;
    top: 40px;
    width: 672px;
    height: 1120px;
    background: var(--cover-bg);
    font-family: "Montserrat", sans-serif;
    color: var(--ink-white);
    box-shadow: 0 10px 30px rgba(0,0,0,0.25);
  }
  .photo-strip {
    position: absolute;
    left: 36px;
    right: 16px;
    top: 22px;
    height: 222px;
    display: flex;
    gap: 10px;
  }
  .photo-tile {
    flex: 1;
    height: 100%;
  }
  .photo-tomatoes { background: linear-gradient(160deg, #1f3a22 0%, #2d4a2a 45%, #a3231b 60%, #223c24 100%); }
  .photo-green-tomatoes { background: linear-gradient(170deg, #223a20 0%, #6f8a4a 50%, #9fb27a 70%, #2a3e24 100%); }
  .photo-path { background: linear-gradient(180deg, #4b5a3a 0%, #6e6a55 40%, #a9a08c 75%, #5b6b43 100%); }
  .photo-carrots { background: linear-gradient(170deg, #3f5a2a 0%, #6a3f22 45%, #b2582a 70%, #3a2616 100%); }

  .title-block {
    position: absolute;
    left: 36px;
    right: 16px;
    top: 280px;
    text-align: center;
  }
  .title-main {
    margin: 0;
    font-weight: 800;
    font-size: 76px;
    line-height: 1;
    letter-spacing: -1px;
  }
  .title-main .accent { color: var(--leaf-green); }
  .title-main .plain { color: var(--ink-white); }
  .title-second {
    margin: 6px 0 0;
    font-weight: 400;
    font-size: 96px;
    line-height: 1;
    color: var(--leaf-green);
    letter-spacing: -1px;
  }
  .subtitle {
    margin: 14px 0 0;
    font-weight: 300;
    font-size: 48px;
    line-height: 1.3;
    letter-spacing: -1px;
  }
  .tagline-band {
    position: absolute;
    left: 36px;
    right: 16px;
    top: 614px;
    height: 148px;
    background: var(--band-red);
    display: flex;
    align-items: center;
    justify-content: center;
    text-align: center;
    font-weight: 400;
    font-size: 19.5px;
    line-height: 1.4;
    text-transform: uppercase;
  }
  .tagline-band p { margin: 0; }
  .harvest-photo {
    position: absolute;
    left: 36px;
    right: 16px;
    top: 762px;
    height: 352px;
    background:
      radial-gradient(circle at 60% 40%, #e98a1e 0%, rgba(233,138,30,0) 35%),
      radial-gradient(circle at 35% 70%, #f09a28 0%, rgba(240,154,40,0) 30%),
      linear-gradient(150deg, #3f7a24 0%, #5e8f2c 35%, #d47a1a 60%, #2f5a1c 100%);
  }
</style>
</head>
<body>
  <main class="book-cover">
    <div class="photo-strip">
      <div class="photo-tile photo-tomatoes" role="img" aria-label="Photo of ripe red tomatoes on the vine"></div>
      <div class="photo-tile photo-green-tomatoes" role="img" aria-label="Photo of unripe green tomatoes among leaves"></div>
      <div class="photo-tile photo-path" role="img" aria-label="Photo of a paved garden path lined with plants"></div>
      <div class="photo-tile photo-carrots" role="img" aria-label="Photo of freshly pulled carrots with soil"></div>
    </div>

    <header class="title-block">
      <h1 class="title-main"><span class="accent">ROOT</span><span class="plain">ED</span></h1>
      <p class="title-second">PLOTS</p>
      <p class="subtitle">A SIMPLE HANDBOOK<br>FOR NEWCOMERS</p>
    </header>

    <section class="tagline-band">
      <p>Zero Skills Required,<br>Easy-Care Methods For A Greener<br>And Nature Kind Yard That Flourishes,<br>Also On Tiny Balconies</p>
    </section>

    <div class="harvest-photo" role="img" aria-label="Photo of harvested oranges among green leaves"></div>
  </main>
</body>
</html>
```